Asset tracing and investigation firm requires marketing brochure for services

We need a professional looking brochure with layout that supports the text that we have already drafted, is easy on the eye and can easily be navigated by clients either electronic/screen format or printed format. The wording is not finalised and all aspects need to be remain editable (including the logo and picture(s)) - preferably in Word or similarly accessible format.

```html
<!DOCTYPE html>
<html lang="en">
<head>
<meta charset="utf-8">
<title>Veritrace – Asset Tracing Services Brochure</title>
<link rel="stylesheet" href="https://fonts.googleapis.com/css2?family=Montserrat:wght@400;600;700&family=Open+Sans:ital,wght@0,400;0,600;0,700;1,700&family=Cinzel:wght@500&display=swap">
<style>
:root{
  --navy:#1d3c8f;
  --navy-dark:#142c6e;
  --gold:#e6b11f;
  --ink:#3b3f4a;
  --paper:#ffffff;
  --stage:#e9eaec;
  --table-row:#c9dbe6;
  --table-alt:#b5cedd;
  --teal:#5aa9c2;
}
*{box-sizing:border-box;margin:0;padding:0}
html,body{width:1200px;height:4000px;overflow:hidden;background:var(--stage)}
body{font-family:"Open Sans",Arial,sans-serif;color:var(--ink);position:relative}
.spread{position:absolute;left:40px;width:1120px;height:540px;background:var(--paper);box-shadow:0 4px 18px rgba(0,0,0,.12);display:flex}
.spread--cover{top:340px}
.spread--about{top:1730px}
.spread--pricing{top:3120px}
.page{position:relative;width:560px;height:540px;overflow:hidden}
.page + .page{border-left:1px solid #e4e6ea}

.brand{font-family:"Montserrat",Arial,sans-serif;font-weight:700;color:var(--navy);letter-spacing:1px;display:flex;align-items:center;gap:7px;white-space:nowrap}
.brand::before{content:"";width:10px;height:10px;background:var(--gold)}
.brand--lg{font-size:30px}
.brand--md{font-size:26px}
.brand--sm{font-size:16px}
.brand--sm::before{width:7px;height:7px}

/* cover spread */
.back-contact{position:absolute;left:60px;bottom:56px;display:flex;align-items:center;gap:22px}
.phone{display:flex;align-items:center;gap:6px;font-family:"Montserrat",sans-serif;font-weight:600;font-size:15px;color:var(--navy);white-space:nowrap}
.contact-list{font-size:10px;color:var(--navy);line-height:1.7;white-space:nowrap}
.contact-list div{display:flex;align-items:center;gap:6px}
.cover-photo{position:absolute;left:0;top:0;width:560px;height:400px;background:linear-gradient(160deg,#2d5fae 0%,#8fb4dc 35%,#cfd6dc 60%,#6f7680 100%)}
.cover-band{position:absolute;left:0;bottom:0;width:560px;height:140px;display:flex}
.cover-band .brand-cell{width:200px;display:flex;align-items:center;justify-content:center}
.cover-band .title-cell{flex:1;background:var(--navy);color:#fff;display:flex;flex-direction:column;justify-content:center;padding-left:24px}
.cover-title{font-family:"Cinzel",serif;font-weight:500;font-size:22px;letter-spacing:1px;white-space:nowrap}
.cover-web{font-size:10px;margin-top:6px;align-self:flex-end;margin-right:26px}

/* text styles */
.heading{font-family:"Montserrat",Arial,sans-serif;font-size:15px;color:var(--navy);font-weight:400;letter-spacing:.3px}
.heading b{font-weight:700}
.body{font-size:7.6px;line-height:1.55;color:var(--ink)}
.body + .body{margin-top:6px}

.side-strip{position:absolute;left:0;top:0;width:34px;height:100%;background:linear-gradient(180deg,#274f9e,#142c6e 60%,#1d3c8f)}
.section{position:absolute;left:64px;right:36px;display:flex;gap:12px}
.icon-dot{flex:none;width:40px;height:40px;border-radius:50%;background:var(--gold);display:flex;align-items:center;justify-content:center}
.section h3{font-family:"Montserrat",sans-serif;font-weight:400;font-size:15px;color:var(--navy);margin:6px 0 4px}
.section h3 b{font-weight:700}

.page-footer{position:absolute;left:0;right:0;bottom:0;height:42px;display:flex;align-items:center;justify-content:space-between;padding:0 24px 0 64px}
.web-pill{display:flex;align-items:center;gap:6px;background:var(--navy);color:#fff;font-size:8.5px;font-weight:600;padding:3px 4px 3px 18px;border-radius:10px;white-space:nowrap}
.web-pill::after{content:"";width:10px;height:10px;border-radius:50%;background:var(--gold)}

.reports{position:absolute;left:34px;top:40px;width:320px}
.reports .heading{margin-bottom:12px}
.ticks{list-style:none;margin:12px 0}
.ticks li{display:flex;gap:8px;font-size:7.4px;font-weight:700;color:var(--ink);line-height:1.45;margin-bottom:8px}
.ticks svg{flex:none;margin-top:1px}
.lab-photo{position:absolute;right:0;top:0;width:180px;height:100%;background:linear-gradient(180deg,#e4eef4 0%,#b6d3e0 45%,#6fa8bf 100%);border-left:10px solid var(--navy)}
.lab-photo .web-pill{position:absolute;right:14px;bottom:14px}

/* pricing */
.pricing{position:absolute;left:34px;top:40px;right:30px}
.price-table{width:100%;margin-top:18px;border-collapse:collapse;font-size:5.6px;line-height:1.45;color:var(--ink);table-layout:fixed}
.price-table th{background:var(--navy);color:#fff;font-family:"Montserrat",sans-serif;font-size:5.6px;font-weight:700;text-align:left;padding:6px 5px;height:30px;vertical-align:top}
.price-table td{background:var(--table-row);padding:6px 5px;vertical-align:top;height:250px}
.price-table td:nth-child(even){background:var(--table-alt)}
.price-table td:last-child{background:var(--teal);color:#fff}
.price-table tr.price td{height:auto;font-weight:700;font-size:6.5px;color:var(--navy);background:#dfe9f0}
.price-table tr.price td:last-child{background:#dfe9f0}
.tiers{position:absolute;left:28px;top:40px;width:300px}
.tier{margin-top:10px}
.tier-name{font-weight:700;font-style:italic;color:var(--navy);font-size:9.5px;margin-right:4px}
.director{position:absolute;right:0;top:0;width:210px;height:100%;background:var(--navy);color:#fff;padding:34px 18px}
.director h2{font-family:"Montserrat",sans-serif;font-size:14px;font-weight:400;line-height:1.3}
.director h2 b{font-weight:700}
.director-top{display:flex;gap:10px;margin-top:14px}
.portrait{flex:none;width:64px;height:84px;background:linear-gradient(180deg,#d6d9de,#8d949e)}
.director-name{font-family:"Montserrat",sans-serif;font-weight:700;color:var(--gold);font-size:9px;margin-bottom:4px}
.director .body{color:#e6ebf5;font-size:6.4px}
.director .web-pill{position:absolute;right:14px;bottom:14px;background:#fff;color:var(--navy)}
</style>
</head>
<body>

<section class="spread spread--cover">
  <div class="page page--back">
    <div class="back-contact">
      <div class="brand brand--lg">VERITRACE</div>
      <div class="phone">
        <svg width="14" height="14" viewBox="0 0 24 24"><path fill="#1d3c8f" d="M6.6 10.8a15 15 0 0 0 6.6 6.6l2.2-2.2c.3-.3.7-.4 1-.2 1.1.4 2.3.6 3.6.6.6 0 1 .4 1 1V20c0 .6-.4 1-1 1A17 17 0 0 1 3 4c0-.6.4-1 1-1h3.5c.6 0 1 .4 1 1 0 1.3.2 2.5.6 3.6.1.3 0 .7-.2 1z"/></svg>
        0203 555 0148
      </div>
      <div class="contact-list">
        <div><svg width="10" height="10" viewBox="0 0 24 24"><circle cx="12" cy="12" r="10" fill="#1d3c8f"/></svg>enquiries@veritrace.co.uk</div>
        <div><svg width="10" height="10" viewBox="0 0 24 24"><path fill="#1d3c8f" d="M12 2a7 7 0 0 0-7 7c0 5 7 13 7 13s7-8 7-13a7 7 0 0 0-7-7zm0 9.5A2.5 2.5 0 1 1 12 6.5a2.5 2.5 0 0 1 0 5z"/></svg>www.veritrace.co.uk</div>
      </div>
    </div>
  </div>
  <div class="page page--front">
    <div class="cover-photo" role="img" aria-label="Low-angle photograph of glass city towers beside a stone building, with blue and gold square overlays"></div>
    <div class="cover-band">
      <div class="brand-cell"><div class="brand brand--md">VERITRACE</div></div>
      <div class="title-cell">
        <div class="cover-title">ASSET TRACING SERVICES</div>
        <div class="cover-web">www.veritrace.co.uk</div>
      </div>
    </div>
  </div>
</section>

<section class="spread spread--about">
  <div class="page">
    <div class="side-strip" role="img" aria-label="Narrow strip photograph of a city building in blue tones"></div>

    <div class="section" style="top:30px">
      <div class="icon-dot"><svg width="18" height="18" viewBox="0 0 24 24"><circle cx="12" cy="8" r="4" fill="#fff"/><path d="M4 21c0-4.4 3.6-7 8-7s8 2.6 8 7z" fill="#fff"/></svg></div>
      <div><h3>WHO <b>WE ARE:</b></h3>
        <p class="body">Veritrace are the asset tracing and investigation specialists for legal and corporate clients seeking fixed fee investigations, pre-sue and asset trace reports with fast turnarounds.</p></div>
    </div>

    <div class="section" style="top:112px">
      <div class="icon-dot"><svg width="18" height="18" viewBox="0 0 24 24"><rect x="5" y="4" width="14" height="17" rx="2" fill="#fff"/><path d="M8 10h8M8 14h8M8 18h5" stroke="#e6b11f" stroke-width="1.6"/></svg></div>
      <div><h3>WHAT <b>WE DO:</b></h3>
        <p class="body">We trace assets and gather crucial intelligence to inform your litigation strategy, bridge knowledge gaps, reduce risk and maximise recoveries. Our asset tracing and investigation services leverage advanced open source and human intelligence with specialist wealth profiling techniques and detailed forensic analysis. We recognise the intricacies of medium and larger sized claims and represent maximum investigative insight and case relevance while keeping scope and fees proportionate to the matter in hand.</p></div>
    </div>

    <div class="section" style="top:228px">
      <div class="icon-dot"><svg width="18" height="18" viewBox="0 0 24 24"><rect x="3" y="7" width="18" height="13" rx="2" fill="#fff"/><rect x="9" y="4" width="6" height="4" fill="none" stroke="#fff" stroke-width="2"/></svg></div>
      <div><h3><b>CASES:</b></h3>
        <p class="body">We regularly conduct asset tracing and investigations on matters spanning Commercial Claims &amp; Disputes, Civil Litigation, Financial Fraud, Enforcement of an Order, Claims against a Director (including those on behalf of a Liquidator), Personal Injury, Employee Fraud, Unrepaid Loans, investigation in respect of Bankrupt's Assets (on behalf of a Trustee), Matrimonial and Enforcement of Personal Guarantees.</p></div>
    </div>

    <div class="section" style="top:338px">
      <div class="icon-dot"><svg width="18" height="18" viewBox="0 0 24 24"><path d="M6 3h9l4 4v14H6z" fill="#fff"/><path d="M9 12h7M9 16h7" stroke="#e6b11f" stroke-width="1.6"/></svg></div>
      <div><h3><b>FEES:</b></h3>
        <p class="body">Our fees are fixed and agreed before any work begins, so there are no surprises. Each report is scoped to your matter, budget and deadline, with clear pricing for every level of service, from a simple address trace to a full international investigation on behalf of a Trustee or Liquidator.</p></div>
    </div>

    <div class="page-footer">
      <div class="brand brand--sm">VERITRACE</div>
      <div class="web-pill">www.veritrace.co.uk</div>
    </div>
  </div>

  <div class="page">
    <div class="reports">
      <h2 class="heading">'PRISM' <b>ASSET TRACE REPORTS:</b></h2>
      <p class="body">We have developed a suite of Asset Tracing products to suit various budgets or quantum / nature of claim. In addition to tracing specific assets, the reports seek to help clients to manage certain other risks inherent in litigation / enforcement and exploit cost effective opportunities to maximise the scope for recovery through insight and intelligence. We do that by, in varying case-specific degrees, assessing matters through the prism of Asset Tracing, Wealth Profiling, Modus Operandi and Contextual Analysis.</p>
      <p class="body">We recognise that there is no 'one size fits all' solution and we treat every case on its individual merits and requirements. Nevertheless, our intention for the information that follows is to provide a clear outline for clients as well as a very broad guideline for investigation in the absence of a more formal scoping exercise.</p>
      <p class="body">With that in mind, our 'Prism' Asset Tracing products meticulously piece together our findings from a myriad of sources to provide an overall picture of the subject, circumstances, and context. For relatively basic pre-sue cases, for example, our remit may be to:</p>
      <ul class="ticks">
        <li><svg width="9" height="9" viewBox="0 0 24 24"><circle cx="12" cy="12" r="11" fill="#1d3c8f"/><path d="M7 12l3.5 3.5L17 9" stroke="#fff" stroke-width="2.6" fill="none"/></svg>Trace physical assets such as residential, investment or commercial property, holiday homes, cars and vehicles, inheritance, private limited company business interests and beneficial ownership searches</li>
        <li><svg width="9" height="9" viewBox="0 0 24 24"><circle cx="12" cy="12" r="11" fill="#1d3c8f"/><path d="M7 12l3.5 3.5L17 9" stroke="#fff" stroke-width="2.6" fill="none"/></svg>Conduct wealth profiling analysis on their lifestyle, background, family, trading history, solvency history, employment, and social media analysis</li>
        <li><svg width="9" height="9" viewBox="0 0 24 24"><circle cx="12" cy="12" r="11" fill="#1d3c8f"/><path d="M7 12l3.5 3.5L17 9" stroke="#fff" stroke-width="2.6" fill="none"/></svg>Perform solvency due diligence through judgment, bankruptcy, credit, and other proprietary database searches</li>
      </ul>
      <p class="body">Beyond these basic investigations, and moving through the Prism levels, we assist on more complex cases, trace additional assets (beyond the 'low hanging fruit') and provide intelligence to bridge knowledge gaps.</p>
    </div>
    <div class="page-footer" style="padding-left:34px">
      <div class="brand brand--sm">VERITRACE</div>
    </div>
    <div class="lab-photo" role="img" aria-label="Photograph of a scientist in a laboratory wearing a hairnet and gloves">
      <div class="web-pill">www.veritrace.co.uk</div>
    </div>
  </div>
</section>

<section class="spread spread--pricing">
  <div class="page">
    <div class="pricing">
      <h2 class="heading">'PRISM' <b>PRICE &amp; SERVICE GUIDE:</b></h2>
      <table class="price-table">
        <colgroup><col style="width:16%"><col style="width:20%"><col style="width:20%"><col style="width:24%"><col style="width:20%"></colgroup>
        <thead><tr>
          <th>LOCATE PRISM</th><th>OUTLINE PRISM</th><th>TARGETED PRISM</th><th>EXTENDED PRISM</th><th>GLOBAL PRISM</th>
        </tr></thead>
        <tbody>
          <tr>
            <td>Generally recommended where the primary focus is to trace the whereabouts of the subject.<br><br>Discreet address and property data trace enquiries.<br><br>1 report output.<br><br>Investigation on one key subject.<br><br>Email report with supporting documents.</td>
            <td>Generally recommended for claims of up to £50,000.<br><br>Discreet tier one OSINT enquiries.<br><br>2 skilled analysts working on the case.<br><br>Asset trace investigation on one key subject and connected entities.<br><br>Forensic analysis of key pertinent records.<br><br>Written report with supporting documents.<br><br>Email updates on progress.</td>
            <td>Generally recommended for claims of up to £250,000.<br><br>Discreet tier one &amp; two OSINT enquiries.<br><br>2 to 3 expert analysts working on the case.<br><br>Asset trace investigation on key subjects, current partnerships and directorships.<br><br>Forensic analysis of current corporate interests.<br><br>Written report with supporting documents.<br><br>Regular email progress updates.</td>
            <td>Generally recommended for claims in excess of £250,000.<br><br>Discreet tier one to three OSINT enquiries.<br><br>A senior investigator and expert analyst team on the case.<br><br>Asset trace investigation on key subjects, connected persons, trusts and offshore holdings.<br><br>Forensic wealth profiling and lifestyle analysis.<br><br>Detailed report with full supporting documents.<br><br>Telephone briefings and written updates.</td>
            <td>Generally recommended for complex or overseas matters.<br><br>To be determined as per the specific scope of investigation.</td>
          </tr>
          <tr class="price"><td>£400</td><td>£600</td><td>£900</td><td>£1,200</td><td>POA</td></tr>
        </tbody>
      </table>
    </div>
    <div class="page-footer" style="padding-left:34px">
      <div class="brand brand--sm">VERITRACE</div>
      <div class="web-pill">www.veritrace.co.uk</div>
    </div>
  </div>

  <div class="page">
    <div class="tiers">
      <h2 class="heading">'OSINT' <b>TIERS:</b></h2>
      <div class="tier"><p class="body"><span class="tier-name">Tier One</span>OSINT sources are essential public and proprietary datasets, including Land Registry, Companies House, Electoral Roll records, Consumer Credit files, County Court Judgment Registers, Insolvency Service records, Probate, Director and Shareholder indexes, Planning Portals, Local Business Directories, Historical Address Data, Vehicle Checks, National Newspaper Archives, Social Media Profiles and Telephone Directories.</p></div>
      <div class="tier"><p class="body"><span class="tier-name">Tier Two</span>sources may sit behind paywalls, require more advanced data mining, analysis or represent more time intensive investigation such as Deep Internet, Human Intelligence, Sourced Enquiries, Third Party Credit Agency Enquiries, Local Language Media, Specialist Property Registers, Archived Domain and Website Registration Data and Specialist Trade Publications.</p></div>
      <div class="tier"><p class="body"><span class="tier-name">Tier Three</span>sources, sourced by specialists in their respective fields, require individual expert manipulation, the use of technology, or the deployment of more advanced methods. These include Dark Web Intelligence, Machine Learning Analysis, Physical Attendances, Field Enquiries, International Database Searches, Corporate Registry Searches and Large Data Gathering and Analysis.</p></div>
    </div>
    <div class="page-footer" style="padding-left:28px">
      <div class="brand brand--sm">VERITRACE</div>
    </div>
    <aside class="director">
      <h2>DIRECTOR OF<br><b>ASSET TRACING:</b></h2>
      <div class="director-top">
        <div class="portrait" role="img" aria-label="Portrait photograph of the director in a suit"></div>
        <div>
          <div class="director-name">IAN MARLOW –</div>
          <p class="body">Open source investigations &amp; intelligence specialist. Since beginning his career with a leading firm 12 years ago, Ian has honed his skills in the manipulation of open source intelligence and analysis.</p>
        </div>
      </div>
      <p class="body" style="margin-top:12px">He specialises in intelligence-led desktop and field source forensic investigation in the context of both disputes and corporate matters, and project implementation. As a result, our range of 'Prism' Asset Tracing Reports benefit from his unique skillset and vast experience of working on literally hundreds of UK and international asset tracing cases.</p>
      <p class="body">As well as contentious civil litigation, pre-sue and fraud investigation, Ian's experience also spans business intelligence, KYC / AML, commercial projects and other due diligence, all of which feeds into the scope of our investigations.</p>
      <div class="web-pill">www.veritrace.co.uk</div>
    </aside>
  </div>
</section>

</body>
</html>
```